Design a Consultation and HR Services Website "Shift Pathways"

Consultation and HR Services
I am looking for a design gives the look and feel of Varden Calloway and Ferrovane
we need a high-quality graphics website that looks rich and expensive.
we are working as an affiliate for international consultation firms and sole agent for international HR products.
we are a group of consultants for the Middle East.
we will get the global practices to local practices.

Reason: I am not getting enough options and designs. I am not getting what I was looking for in matter of look and feel. looking for something rich and luxury with black background and rich font. www.blockvault.example www.lucindavarga.example 71dormerplace.example/ www.velquo.example/rd/en/ morvethhouse.example/ www.velquo.example/rd/en/ www.quillen.example/ www.theplaudits.example/ .

Target Market(s)

Corporate all size and industries in GCC

Industry/Entity Type

Management Consulting

Coding

Coded - Design and coding required

Number of Pages Required

5+ page

Font styles to use
Sans Serif
Script

Colors
ffffff
ecf7fb
cee9f5
85cae6
33a6d7
0592cd
000000
848484

Requirements
Must have
• This is the looks and feel that I'm looking for.
• http://www.blockvault.example/?channel=display&subchannel=sitemuse
• http://www.lucindavarga.example/lvny-private/en/
• http://71dormerplace.example/
• http://www.velquo.example/rd/en/
• http://morvethhouse.example/
• http://www.quillen.example/
• http://www.theplaudits.example/
• Home
• Who we are?
• What we do?
• HR & OD Consultation
• Executive Coaching
• Assesment Cemter
• HRIS & Outsourcing
• Testimonials
• Our Partners
• Contact Us
• We need support on Technical righting...

```html
<!DOCTYPE html>
<html lang="en">
<head>
<meta charset="utf-8">
<title>Shift Pathways</title>
<link href="https://fonts.googleapis.com/css2?family=Raleway:wght@300;400;500;600;700&family=Open+Sans:wght@400;600&display=swap" rel="stylesheet">
<style>
:root{
  --black:#000000;
  --blue:#33a6d7;
  --blue-deep:#0592cd;
  --blue-soft:#85cae6;
  --grey:#848484;
  --tile:#6f6f6f;
  --text:#5e5e5e;
  --white:#ffffff;
  --mist:#f3f4f6;
  --footer:#3a3a3a;
}
*{box-sizing:border-box;margin:0;padding:0}
html,body{width:726px;height:1200px;overflow:hidden;background:var(--white)}
body{position:relative;font-family:"Raleway",sans-serif;color:var(--text)}
.abs{position:absolute}

.topbar{left:0;top:0;width:726px;height:64px;background:var(--black);border-top:3px solid var(--blue-soft)}
.brand{left:60px;top:14px;display:flex;align-items:center;gap:6px}
.brand-mark{width:14px;height:14px;background:var(--blue)}
.brand-name{font-family:"Raleway",sans-serif;font-weight:600;font-size:12px;color:var(--blue);letter-spacing:.2px}
.nav{left:335px;top:28px;display:flex;font-family:"Raleway",sans-serif;font-size:7.5px;color:var(--white)}
.nav span{margin-right:37px}
.nav .active{color:var(--blue)}

.hero{left:0;top:64px;width:726px;height:364px;background:linear-gradient(100deg,#3c4654 0%,#6c7a8b 30%,#9aa7b6 55%,#5b6677 80%,#2f3844 100%)}
.hero-title{left:58px;top:176px;font-family:"Raleway",sans-serif;font-weight:700;font-size:45px;color:var(--white);letter-spacing:-.5px}
.hero-sub{left:64px;top:238px;font-family:"Raleway",sans-serif;font-weight:300;font-size:22px;color:var(--white)}
.btn{left:60px;top:286px;width:89px;height:26px;background:var(--blue);color:var(--white);font-family:"Open Sans",sans-serif;font-weight:600;font-size:8.5px;display:flex;align-items:center;justify-content:center;border-radius:2px}
.arrow{top:228px}

.section-title{width:726px;left:0;text-align:center;font-family:"Raleway",sans-serif;font-weight:400;font-size:18px;color:var(--blue)}
.lede{width:726px;left:0;text-align:center;font-family:"Open Sans",sans-serif;font-size:6.6px;line-height:14.5px;color:var(--text)}
.lede-small{font-size:7px;color:var(--text)}

.services{left:0;top:548px;width:726px;height:269px;background:linear-gradient(120deg,#eceef1,#f7f8fa 50%,#e9ecf0)}
.service{width:150px;text-align:center}
.tile{width:76px;height:76px;margin:0 auto;background:var(--tile);display:flex;align-items:center;justify-content:center}
.tile.active{background:var(--blue)}
.service-name{margin-top:10px;font-size:8.5px;color:#444}
.service-name.active{color:var(--blue)}
.service-text{margin-top:5px;font-family:"Open Sans",sans-serif;font-size:6.5px;line-height:13.5px;color:var(--text)}

.project{top:897px;width:139px;height:104px;box-shadow:0 3px 4px rgba(0,0,0,.18)}

.testimonial{left:0;top:1035px;width:726px;height:113px;background:#f6f6f6}
.avatar{left:68px;top:1051px;width:72px;height:72px;border-radius:50%;background:linear-gradient(160deg,#e3e6ea,#b9c2cc);border:3px solid var(--white)}
.quote{left:171px;top:1058px;width:475px;font-family:"Open Sans",sans-serif;font-size:6.5px;line-height:14.5px;color:var(--grey)}
.qmark{font-family:Georgia,serif;font-size:16px;color:#c9c9c9}
.author{left:171px;top:1113px;font-size:6.5px;color:var(--blue)}
.role{left:171px;top:1126px;font-size:7px;color:var(--grey)}

.footer{left:0;top:1148px;width:726px;height:52px;background:var(--footer)}
.foot-links{left:60px;top:1159px;font-family:"Open Sans",sans-serif;font-size:6.5px;color:#e0e0e0}
.copy{left:60px;top:1177px;font-family:"Open Sans",sans-serif;font-size:6.5px;color:#e0e0e0}
.social{left:588px;top:1175px;display:flex;gap:4px}
.social span{width:16px;height:16px;border-radius:50%;background:#6a6a6a}
</style>
</head>
<body>

<header class="abs topbar">
  <div class="abs brand"><span class="brand-mark"></span><span class="brand-name">Shift Pathways</span></div>
  <nav class="abs nav"><span class="active">HOME</span><span>ABOUT US</span><span>SERVICES</span><span>RESOURCES</span><span>CONTACT US</span></nav>
</header>

<section class="abs hero" role="img" aria-label="Business people shaking hands over a desk with a tablet and charts"></section>
<svg class="abs arrow" style="left:26px" width="12" height="36" viewBox="0 0 12 36"><polyline points="10,1 2,18 10,35" fill="none" stroke="rgba(255,255,255,.6)" stroke-width="1"/></svg>
<svg class="abs arrow" style="left:690px" width="12" height="36" viewBox="0 0 12 36"><polyline points="2,1 10,18 2,35" fill="none" stroke="rgba(255,255,255,.4)" stroke-width="1"/></svg>
<h1 class="abs hero-title">SHIFT PATHWAYS</h1>
<p class="abs hero-sub">AT VERO EOS ET ACCUSAMUS AT</p>
<a class="abs btn">READ MORE</a>

<h2 class="abs section-title" style="top:446px">Welcome To Our Company</h2>
<p class="abs lede" style="top:477px;padding:0 80px">Lorem Ipsum es simplemente el texto de relleno de las imprentas y archivos de texto. Lorem Ipsum ha sido el texto de relleno estándar de las industrias desde el año 1500, cuando un impresor (N. del T. persona que se dedica a la imprenta) desconocido usó una galería de textos y los mezcló de tal manera que logró hacer un libro de textos especimen. No sólo sobrevivió 500 años, sino que tambien ingresó como texto</p>

<section class="abs services"></section>
<h2 class="abs section-title" style="top:563px">Our Services</h2>
<p class="abs lede lede-small" style="top:594px">Es simplemente el texto de relleno de las imprentas y archivos de texto. Lorem Ipsum ha sido el texto de relleno estándar de las...</p>

<div class="abs service" style="left:62px;top:634px">
  <div class="tile active"><svg width="32" height="28" viewBox="0 0 32 28"><rect x="1" y="1" width="30" height="19" rx="2" fill="#fff"/><rect x="13" y="20" width="6" height="4" fill="#fff"/><rect x="8" y="24" width="16" height="2" fill="#fff"/></svg></div>
  <div class="service-name active">Services 01</div>
  <div class="service-text">Es simplemente el texto de relleno de<br>las imprentas y archivos de texto.<br>Lorem Ipsum ha sido el...</div>
</div>
<div class="abs service" style="left:212px;top:634px">
  <div class="tile"><svg width="30" height="30" viewBox="0 0 30 30" fill="none" stroke="#fff" stroke-width="2"><path d="M4 8 L11 2 H17 V20 H4 Z"/><path d="M13 12 L19 7 H26 V28 H13 Z"/></svg></div>
  <div class="service-name">Services 02</div>
  <div class="service-text">Es simplemente el texto de relleno de<br>las imprentas y archivos de texto.<br>Lorem Ipsum ha sido el...</div>
</div>
<div class="abs service" style="left:362px;top:626px">
  <div class="tile"><svg width="28" height="28" viewBox="0 0 28 28" fill="none" stroke="#fff" stroke-width="3" stroke-linecap="round"><path d="M8 7 A10 10 0 1 0 20 7"/><line x1="14" y1="2" x2="14" y2="13"/></svg></div>
  <div class="service-name" style="margin-top:18px">Services 03</div>
  <div class="service-text">Es simplemente el texto de relleno de<br>las imprentas y archivos de texto.<br>Lorem Ipsum ha sido el...</div>
</div>
<div class="abs service" style="left:512px;top:634px">
  <div class="tile"><svg width="34" height="30" viewBox="0 0 34 30" fill="none" stroke="#fff"><circle cx="12" cy="17" r="6" stroke-width="5"/><circle cx="12" cy="17" r="10" stroke-width="4" stroke-dasharray="3.5 3.5"/><circle cx="26" cy="8" r="3.5" stroke-width="3"/><circle cx="26" cy="8" r="6" stroke-width="2.5" stroke-dasharray="2.5 2.2"/><circle cx="26" cy="23" r="3" stroke-width="2.5"/><circle cx="26" cy="23" r="5" stroke-width="2" stroke-dasharray="2 2"/></svg></div>
  <div class="service-name">Services 04</div>
  <div class="service-text">Es simplemente el texto de relleno de<br>las imprentas y archivos de texto.<br>Lorem Ipsum ha sido el...</div>
</div>

<h2 class="abs section-title" style="top:831px">Our Projects</h2>
<p class="abs lede lede-small" style="top:862px">Es simplemente el texto de relleno de las imprentas y archivos de texto. Lorem Ipsum ha sido el texto de relleno estándar de las...</p>
<div class="abs project" style="left:60px;background:linear-gradient(135deg,#8db4d6,#3b4f6a)" role="img" aria-label="Two businessmen shaking hands outdoors"></div>
<div class="abs project" style="left:216px;background:linear-gradient(135deg,#d8dcd9,#8b9490)" role="img" aria-label="Office workers at their desks"></div>
<div class="abs project" style="left:372px;background:linear-gradient(135deg,#c9c3b8,#6f6a63)" role="img" aria-label="Team meeting around a table with documents"></div>
<div class="abs project" style="left:527px;background:linear-gradient(135deg,#e6e8ea,#9ea6ad)" role="img" aria-label="Businesswoman at an office desk"></div>

<section class="abs testimonial"></section>
<div class="abs avatar" role="img" aria-label="Portrait of the executive giving the testimonial"></div>
<span class="abs qmark" style="left:157px;top:1050px">“</span>
<p class="abs quote">Lorem Ipsum es simplemente el texto de relleno de las imprentas y archivos de texto. Lorem Ipsum ha sido el texto de relleno estándar de las industrias desde el año 1500, cuando un impresor (N. del T. persona que se dedica a la imprenta) desconocido usó una galería On the other hand, we denounce moment, so blinded by desire, that they cannot foresee...</p>
<span class="abs qmark" style="left:633px;top:1084px">”</span>
<span class="abs author">MARLO VENNING</span>
<span class="abs role">Marketing Executive</span>

<footer class="abs footer"></footer>
<div class="abs foot-links">HOME &nbsp;/&nbsp; ABOUT US &nbsp;/&nbsp; SERVICES &nbsp;/&nbsp; RESOURCES &nbsp;/&nbsp; CONTACT US</div>
<div class="abs copy">2015 © Copy right .Shift Pathways .all right reserved</div>
<div class="abs social"><span></span><span></span><span></span><span></span></div>

</body>
</html>
```